Plakat-Design für Chor und Blasorchester
Zielgruppe
Konzert eines Orchesters zusammen mit drei Chören.
Zielgruppe Musikinteressierte allen Alters
(Alter der Musiker/Sänger 15-85)
Aufgabenstellung
PLakat wird in erster Linie in A3 und A4 gedruck.
Vermutlich machen wir auch Flyer

```html
<!DOCTYPE html>
<html lang="de">
<head>
<meta charset="utf-8">
<title>Ohrwürmer – Konzertplakat</title>
<link href="https://fonts.googleapis.com/css2?family=Cinzel:wght@400;700&family=Marcellus&display=swap" rel="stylesheet">
<style>
  :root {
    --stage: #f1f1f1;
    --paper: #f1efee;
    --ink: #5a3423;
    --ink-soft: #8a5a40;
    --sepia-deep: #7a4f33;
    --sepia-dark: #a9784f;
    --sepia-mid: #d7a677;
    --sepia-light: #ecd7c0;
  }
  html, body { margin: 0; padding: 0; width: 1028px; height: 1200px; overflow: hidden; background: var(--stage); }
  .poster {
    position: absolute; left: 110px; top: 29px; width: 807px; height: 1141px;
    background: var(--paper); overflow: hidden;
    box-shadow: 0 2px 10px rgba(0,0,0,.18);
    font-family: "Marcellus", serif; color: var(--ink);
  }
  .portraits {
    position: absolute; left: 0; top: 0; width: 807px; height: 700px;
    background:
      radial-gradient(ellipse 22% 30% at 27% 30%, rgba(122,79,51,.75), transparent 75%),
      radial-gradient(ellipse 24% 32% at 66% 40%, rgba(90,58,38,.8), transparent 75%),
      radial-gradient(ellipse 32% 26% at 25% 62%, rgba(169,120,79,.7), transparent 78%),
      radial-gradient(ellipse 36% 28% at 64% 74%, rgba(169,120,79,.65), transparent 78%),
      radial-gradient(ellipse 70% 60% at 50% 48%, var(--sepia-light), rgba(236,215,192,.5) 65%, transparent 90%);
    -webkit-mask-image: linear-gradient(to bottom, #000 80%, transparent 100%);
            mask-image: linear-gradient(to bottom, #000 80%, transparent 100%);
  }
  .wash {
    position: absolute; width: 230px; height: 320px; top: 800px;
    background: radial-gradient(ellipse at center, rgba(215,166,119,.6), rgba(236,215,192,.3) 55%, transparent 75%);
  }
  .wash--left { left: -70px; }
  .wash--right { right: -70px; }
  .type { position: absolute; left: 0; top: 0; width: 807px; height: 1141px; }
  .title { font-family: "Cinzel", serif; font-size: 112px; fill: var(--ink); }
  .subtitle { font-family: "Marcellus", serif; font-size: 22px; fill: var(--ink-soft); }
  .date { font-family: "Cinzel", serif; font-weight: 700; font-size: 22px; fill: var(--ink); }
  .venue { font-family: "Marcellus", serif; font-size: 16px; fill: var(--ink-soft); }
  .block { position: absolute; text-align: center; }
  .name { font-family: "Cinzel", serif; font-weight: 700; font-size: 16px; letter-spacing: -.3px; line-height: 20px; }
  .place { font-size: 11px; line-height: 14px; color: var(--ink-soft); }
  .orchestra { left: 0; width: 807px; top: 829px; }
  .choir { top: 872px; width: 220px; }
  .choir--1 { left: 72px; } .choir--2 { left: 290px; } .choir--3 { left: 501px; }
  .lead { left: 0; width: 807px; top: 932px; }
  .lead .place { margin-bottom: 2px; }
  .emblem { position: absolute; left: 373px; top: 1015px; width: 60px; height: 60px; }
  .rule { position: absolute; left: 40px; right: 43px; top: 1106px; border-top: 1.5px dotted var(--ink-soft); }
  .admission {
    position: absolute; left: 40px; right: 43px; top: 1113px;
    display: flex; justify-content: space-between; font-size: 11px; color: var(--ink-soft);
  }
  .admission b { font-family: "Cinzel", serif; font-weight: 700; color: var(--ink); }
</style>
</head>
<body>
<main class="poster">
  <div class="portraits" role="img" aria-label="Sepia-Porträts zweier Komponisten über Notenblättern mit Aquarellflecken"></div>
  <div class="wash wash--left"></div>
  <div class="wash wash--right"></div>

  <svg class="type" viewBox="0 0 807 1141">
    <text class="title" x="42" y="728" textLength="722" lengthAdjust="spacingAndGlyphs">OHRWÜRMER</text>
    <text class="subtitle" x="45" y="779" textLength="715" lengthAdjust="spacingAndGlyphs">VON VARELLI BIS COLMAN FÜR CHOR UND SINFONISCHES BLASORCHESTER</text>
    <text class="date" x="40" y="1035" textLength="311" lengthAdjust="spacingAndGlyphs">19. NOVEMBER 2017, 17:00 UHR</text>
    <text class="venue" x="40" y="1057">KIRCHE ST. LORENZ</text>
    <text class="venue" x="40" y="1078">KONSTANZ</text>
    <text class="date" x="764" y="1035" text-anchor="end" textLength="313" lengthAdjust="spacingAndGlyphs">26. NOVEMBER 2017, 17:00 UHR</text>
    <text class="venue" x="764" y="1057" text-anchor="end">TALKIRCHE</text>
    <text class="venue" x="764" y="1078" text-anchor="end">WINTERTHUR</text>
  </svg>

  <div class="block orchestra"><div class="name">MUSIKVEREIN HALDENRIED (D)</div></div>

  <div class="block choir choir--1"><div class="name">CANTABILE CHOR</div><div class="place">KONSTANZ (D)</div></div>
  <div class="block choir choir--2"><div class="name">LE C(H)OEUR VIVACE</div><div class="place">MATTENAU (CH)</div></div>
  <div class="block choir choir--3"><div class="name">GEMISCHTER CHOR</div><div class="place">LINDENAU (CH)</div></div>

  <div class="block lead"><div class="place">LEITUNG:</div><div class="name">GRETA FELDHAUS / JONAS BRENNER</div></div>

  <svg class="emblem" viewBox="0 0 60 60" role="img" aria-label="Ornament">
    <circle cx="30" cy="30" r="28" fill="var(--sepia-mid)" opacity=".5"/>
  </svg>

  <div class="rule"></div>
  <div class="admission">
    <b>E</b><b>I</b><b>N</b><b>T</b><b>R</b><b>I</b><b>T</b><b>T</b><span>&nbsp;</span><b>F</b><b>R</b><b>E</b><b>I</b><span>&nbsp;</span><span>–</span><span>&nbsp;</span><span>S</span><span>P</span><span>E</span><span>N</span><span>D</span><span>E</span><span>&nbsp;</span><span>F</span><span>R</span><span>E</span><span>U</span><span>N</span><span>D</span><span>L</span><span>I</span><span>C</span><span>H</span><span>&nbsp;</span><span>E</span><span>R</span><span>B</span><span>E</span><span>T</span><span>E</span><span>N</span>
  </div>
</main>
</body>
</html>
```